PSD web site UI

I need a PSD of a web site interface that I can use to build a theme with, which will be used on www.plovix.com, an up-and-coming CMS platform that I developed.

Follow the specifications included within the RAR file download below, and use the included PSD as a reference to make your own unique UI design.

Winners will be chosen based on how clean & professional the design looks, by how many unique panel designs are included within the UI, and by how large of a target market could actually use the design for their business web site.

Contest winners will only need to provide their PSD as completed work.

Download the PSD mockup at the bottom of this page to get started right away!

Target Market(s)

small businesses and freelance designers, photographers & artists.

Industry/Entity Type

Business

Requirements
Must have
• Your PSD can have any color scheme you want. It can be light, dark, green, blue, multi-colored, paper, metallic, glossy, shiny, solid, gradients, or any theme you can imagine. Be creative, but keep the design looking Web 2.0 & professional. The width of your design can be 960 pixels wide like in the provided mockup PSD, or it can be a 100% width design if you'd like.

-
Panels
-
Each theme requires a minimum of 5 panel designs, which is basically a box that can stretch to a specific width or that stretches to 100% width of the web site. These 5 panels include a header, body, footer, child (that is placed within the body panel), and an alternative body panel. Of course, you can create as many panels as you like to create a more custom theme. Your panels do not have to look like the ones provided in the PSD mockup. They don't have to be completely square with round corners. They could be a bubbly cloud, or wavy, or include garnish around the edges, or be torn paper, or anything you like. Also, you can include a title within some of your panels, which is basically a header design with text at the top of the panel.

Each panel must contain a set of elements that fit the design of the panel. The body of your design should also include this set of elements. These elements include at least one menu, a set of buttons, lorum ipsum text & an anchor link, and form elements, such as a textbox, dropdown, & checkbox.

-
body
-
The body of your design should use a texture, gradient, solid color, or a background image that stretches 100% width. If you separate the body of your design into sectioned rows, each row will be treated like a panel.

-
Dashboard section
-
After a user logs into their account on Plovix.com, they manage their web site via a dashboard. This dashboard has a complex design, but can be partially customized. All elements within the header of the dashboard can be rearranged. This includes the title, screenshot, section title, and section menu. The main menu on the left contains a list of sections within the dashboard, which when clicked, will load the section title & menu in the dashboard header, and load the section page within the body of the dashboard.

Dashboard Icons:
The main menu & other menus within the dashboard contain icons. You can create your own custom icon library to use with your theme if you'd like, and the toolkit comes with a complete set of icons to use if you choose not to create your own library.

Dashboard body:
Each row within the dashboard body (options, search, results, paging) can use a panel design, but the entire dashboard body can also use a panel design as well, so you could design your dashboard body to use just one encompassing panel instead of separate panels for each row if you wanted.

-
Buttons
-
Each panel must contain a set of buttons. Each button requires a regular design as well as a mouse-over design. These types of buttons include: default, apply, cancel, previous, next, and delete (delete should stay small like a "close window" button).

-
Menus
-
Each menu requires a mouse-over design & selected item design.
You can make many types of menus; vertical, horizontal, small, and large.
Each item in the menu can be uniquely designed to create a sequence of menu items. For example, grey, white, grey, white, etc..

-
Photo Gallery
-
each photo container can be uniquely designed, creating a sequence of designs in a list.

-
Comments
-
each comment post can be uniquely designed, creating a sequence of designs in a list.
This will be used for comments as well as twitter feeds.

-
Blog Entries
-
Create designs for a blog summary list & a blog entry details.

Each blog entry (summary or details) can be uniquely designed, creating a sequence of designs in a list.

You could display a title, date created, tag words, summary, and the entry text, but you don't have to display all fields.

-
Product List
-
Products can be displayed many different ways:

product details, list grid, list rows, or even featured products list (with a flashy design).

You can display the product title, price, sale price & sale end date, description, photo & photo gallery, add to cart button, and view product details button. You don't have to display all fields for each design. You could show just a photo & title with summary & no price, or just a photo & title, or just the photo if you wanted.

-
Form elements
-
The textbox can look completely custom, have rounded corners, a textured background, or look plain if you want. The other form elements on the other hand can only be manipulated by CSS, so are very limited in design. Only border color, background color, and text color can be changed. The drop down box can have a custom drop down arrow though.

-
Header Panel
-
Requires a horizontal menu system that can be used for the web site's main menu

-
Footer Panel
-
The footer should be 100% width. Many web sites these days have very creative footers.
Should not have
• Don't use the mockup to just make color changes. I want a completely custom design that uses the structure of the mockup, but has a unique theme to the design, such as paper, dark grungy, cartoonish, hand-drawn, etc. Impress me & impress yourself!

```html
<!DOCTYPE html>
<html lang="en">
<head>
<meta charset="utf-8">
<title>Plovix — Dashboard Theme</title>
<link href="https://fonts.googleapis.com/css2?family=Open+Sans:wght@300;400;600;700&display=swap" rel="stylesheet">
<style>
:root{
  --page:#e9eaeb;
  --sheet:#ffffff;
  --blue:#1f7fc9;
  --blue-dark:#0f62a8;
  --blue-light:#4aa5e6;
  --orange:#f7931e;
  --orange-dark:#e8780a;
  --green:#5cae1f;
  --ink:#444;
  --muted:#8a8a8a;
  --title-blue:#1d77bd;
  --panel-line:#dfe5ea;
  --panel-bg:#f6f9fb;
  --dark:#3c3c3c;
  --dark-2:#2e2e2e;
}
*{box-sizing:border-box;margin:0;padding:0}
html,body{width:1200px;height:3056px;overflow:hidden}
body{position:relative;background:var(--page);font-family:"Open Sans",Arial,sans-serif;color:var(--ink)}
.abs{position:absolute}
.header{left:0;top:0;width:1200px;height:147px;background:linear-gradient(#4aa8ea,#1a7dcb 60%,#1570bd);border-top:8px solid #6cc0f4}
.logo{left:72px;top:36px;font-weight:300;font-size:58px;letter-spacing:3px;color:#fff}
.main-nav{left:510px;top:70px;display:flex;list-style:none}
.main-nav li{color:#fff;font-size:21px;padding:0 22px;border-left:1px solid rgba(255,255,255,.35)}
.main-nav li:first-child{border-left:none}
.sheet{left:45px;top:147px;width:1112px;height:2746px;background:var(--sheet)}
.panel{background:linear-gradient(#fff,var(--panel-bg));border:2px solid var(--panel-line);border-radius:8px}
.side-menu{left:63px;top:183px;width:265px}
.side-menu h3{height:47px;background:linear-gradient(#fba436,var(--orange-dark));color:#fff;font-weight:400;font-size:20px;padding:10px 32px;border-radius:6px 6px 0 0}
.side-menu ul{list-style:none;border:1px solid #ddd;border-top:none}
.side-menu li{height:45px;border-bottom:1px solid #e3e3e3;display:flex;align-items:center;padding-left:34px;font-size:15px;color:#444}
.side-menu li.active-page{background:#fdf1e5}
.side-menu li.selected{background:linear-gradient(#7cc42c,var(--green));color:#fff;font-weight:600}
.ico{display:inline-block;width:18px;height:16px;border:2px solid #6b7a88;border-radius:2px;margin-right:17px;flex:none}
.selected .ico{border-color:#fff;background:#2d6a10}
.profile{left:346px;top:183px;width:789px;height:218px}
.shot{left:23px;top:19px;width:240px;height:167px;border:1px solid #ccc;border-radius:8px;background:#fff;padding:8px}
.shot div{width:100%;height:100%;border-radius:4px;background:linear-gradient(#555,#888 30%,#48c8e8 55%,#a8ecf7)}
.profile-name{left:290px;top:22px;font-size:29px;color:var(--title-blue)}
.round-btn{display:inline-block;width:26px;height:26px;border:2px solid var(--title-blue);border-radius:50%;vertical-align:middle;margin-left:6px}
.book{left:290px;top:78px;font-size:29px;color:#333;display:flex;align-items:center}
.book-mark{width:34px;height:38px;background:var(--green);border-radius:4px;margin-right:10px}
.new-entry{left:290px;top:145px;font-size:13px;color:#3a8a1a;display:flex;align-items:center}
.plus{width:20px;height:20px;border-radius:50%;background:var(--green);color:#fff;font-size:16px;line-height:19px;text-align:center;margin-right:6px;font-weight:700}
.folder{left:346px;top:418px;width:789px;height:138px;overflow:hidden}
.folder-label{left:32px;top:36px;color:var(--orange);font-size:21px}
.select{left:102px;top:30px;width:285px;height:40px;border:1px solid #ccc;background:#fff;font-size:13px;color:#999;padding:10px 14px}
.select span{position:absolute;right:-1px;top:-1px;width:36px;height:40px;background:#6b8d1e}
.select span svg{margin:13px 10px}
.folder-bar{left:0;top:89px;width:789px;height:47px;background:linear-gradient(#fba436,var(--orange-dark));display:flex;align-items:center;padding-left:30px;gap:22px}
.folder-bar div{color:#fff;font-size:13px;display:flex;align-items:center}
.folder-bar i{width:26px;height:26px;border-radius:50%;background:#fff;margin-right:8px;display:inline-block}
.search{left:346px;top:585px;width:789px;height:102px}
.search-input{left:37px;top:28px;width:334px;height:42px;border:1px solid #c8c8c8;border-radius:6px 0 0 6px;background:#fff;font-size:13px;font-style:italic;color:#999;padding:11px 18px}
.search-btn{left:369px;top:28px;width:104px;height:42px;background:linear-gradient(#49b4ee,#1d8dd6);border-radius:0 6px 6px 0;color:#fff;font-size:19px;text-align:center;line-height:42px}
.results{left:346px;top:705px;width:789px;height:242px}
.result{left:0;width:785px;height:120px;padding:25px 0 0 66px}
.result + .result{border-top:2px solid var(--panel-line)}
.check{left:28px;top:32px;width:20px;height:20px;border:1px solid #aaa;border-radius:3px;background:#fff}
.result h4{font-size:19px;font-weight:400;color:var(--title-blue)}
.result p{font-size:15px;color:var(--blue-light);margin-top:4px}
.close{right:24px;top:48px}
.dark-bar{left:63px;top:974px;width:1072px;height:140px;background:linear-gradient(#4a4a4a,var(--dark-2));border-radius:6px}
.toolbar{display:flex;gap:24px;font-size:14px;color:#fff;align-items:center}
.toolbar span{display:flex;align-items:center}
.toolbar .ico{border-color:#cfd6dc;width:16px;height:14px;margin-right:8px}
.dark-bar .toolbar{left:44px;top:32px}
.dark-bar p{left:44px;top:74px;width:570px;font-size:13px;color:#ddd;line-height:22px}
.dark-nav{left:609px;top:0;display:flex;height:140px}
.dark-nav div{width:114px;border-left:1px solid #5c5c5c;color:#fff;font-size:21px;display:flex;align-items:center;justify-content:center}
.dark-nav div:nth-child(2){width:102px}
.dark-nav div:nth-child(3){width:110px}
.x-box{width:16px;height:16px;border:1px solid #aaa;display:inline-block;margin-left:8px;position:relative}
.x-box::after{content:"×";position:absolute;left:2px;top:-6px;font-size:16px;color:#aaa}
.gallery{left:63px;top:1141px;width:1072px;height:269px}
.gallery h3{left:48px;top:34px;font-size:22px;font-weight:400;color:var(--title-blue)}
.gallery .toolbar{left:550px;top:32px;color:#555}
.gallery .toolbar .ico{border-color:#5b6b7a}
.photo{top:90px;width:203px;height:140px;border:1px solid #ddd;padding:6px;background:#fff;border-radius:6px}
.photo div{width:100%;height:100%;border-radius:3px}
.comments{left:67px;top:1436px;width:758px;height:371px;overflow:hidden}
.avatar{left:30px;width:102px;height:102px;border:1px solid #ddd;background:#fff;padding:6px;border-radius:4px}
.avatar div{width:100%;height:100%;background:linear-gradient(#e7e7e7,#c8c8c8)}
.bubble{left:165px;width:532px;border:1px solid #e0e0e0;border-radius:6px;background:#fff;box-shadow:0 2px 4px rgba(0,0,0,.06)}
.bubble p{font-size:14px;color:#666;line-height:24px;padding:18px 26px 14px}
.bubble small{display:block;background:#ececec;font-size:13px;color:#888;padding:8px 26px}
.comment-bar{left:0;top:324px;width:758px;height:47px;background:linear-gradient(#3a9ee3,var(--blue-dark));border-top:4px solid #9fd4f6}
.small-btn{position:absolute;top:10px;height:26px;padding:0 16px;background:var(--blue-dark);border:1px solid #5fb0ea;border-radius:4px;color:#fff;font-size:13px;line-height:24px}
.calendar{left:849px;top:1434px;width:282px;border:1px solid #ccc;background:#fff}
.calendar h4{height:43px;background:linear-gradient(#fba436,var(--orange-dark));color:#fff;font-weight:600;font-size:15px;text-align:center;line-height:43px;position:relative}
.calendar table{width:100%;border-collapse:collapse;font-size:14px}
.calendar th{font-weight:400;color:#666;height:27px;background:#f3f3f3;border:1px solid #ddd}
.calendar td{text-align:center;height:31px;border:1px solid #ddd;color:#444}
.calendar td.off{color:#aaa}
.calendar td.today{background:#2b2b2b;color:#fff}
.leave{left:67px;top:1833px;width:758px;height:363px}
.leave h3{left:38px;top:28px;font-size:22px;font-weight:400;color:#444}
.field{height:40px;border:1px solid #cfcfcf;border-radius:6px;background:#fff;font-size:13px;font-style:italic;color:#999;padding:10px 18px}
.submit{left:37px;top:296px;width:142px;height:42px;background:linear-gradient(#fba436,var(--orange-dark));border-radius:6px;color:#fff;font-weight:700;font-size:14px;text-align:center;line-height:42px}
.post{top:2224px;width:338px;height:302px;padding:28px 26px}
.post h4{font-size:20px;font-weight:400;color:#333;line-height:28px}
.post p{font-size:13px;color:#888;line-height:24px;margin-top:10px}
.post em{display:block;font-style:normal;font-size:13px;color:var(--orange-dark);margin-top:2px}
.learn{display:inline-block;margin-top:18px;padding:0 20px;height:36px;line-height:36px;background:linear-gradient(#fba436,var(--orange-dark));border-radius:5px;color:#fff;font-size:14px;font-weight:600}
.products{left:67px;top:2556px;width:1058px;height:296px}
.product{top:29px;width:232px;height:224px;border:1px solid #ddd;border-radius:6px;background:#fff;box-shadow:0 2px 5px rgba(0,0,0,.08)}
.product .pic{position:absolute;left:30px;top:14px;width:172px;height:126px;border-radius:6px}
.product h5{position:absolute;left:22px;top:150px;font-size:13px;font-weight:400;color:#444}
.product b{position:absolute;left:22px;top:170px;font-size:23px;font-weight:400;color:#333}
.cart{position:absolute;left:122px;top:172px;width:96px;height:30px;background:linear-gradient(#fba436,var(--orange-dark));border-radius:4px;color:#fff;font-size:12px;font-weight:700;text-align:center;line-height:30px}
.footer{left:0;top:2893px;width:1200px;height:163px;background:var(--dark)}
.footer-logo{left:40px;top:38px;font-size:48px;font-weight:300;letter-spacing:2px;color:#fff}
.footer-copy{left:42px;top:104px;font-size:12px;color:#999}
.footer .toolbar{font-size:14px;color:#ddd;gap:22px}
</style>
</head>
<body>

<header class="abs header">
  <div class="abs logo">PLOVIX</div>
  <ul class="abs main-nav"><li>Dashboard</li><li>Community</li><li>Developers</li><li>Support</li></ul>
</header>

<div class="abs sheet"></div>

<nav class="abs side-menu">
  <h3>Select Menu</h3>
  <ul>
    <li class="active-page"><i class="ico"></i>Pages</li>
    <li><i class="ico"></i>Media</li>
    <li><i class="ico"></i>Messages</li>
    <li><i class="ico"></i>Analytics</li>
    <li><i class="ico"></i>Site Map</li>
    <li><i class="ico"></i>Settings</li>
    <li><i class="ico"></i>Install Apps</li>
    <li class="selected"><i class="ico"></i>Blog Book</li>
  </ul>
</nav>

<section class="abs panel profile">
  <div class="abs shot"><div role="img" aria-label="Website screenshot thumbnail"></div></div>
  <div class="abs profile-name">Marcus Hale <i class="round-btn"></i><i class="round-btn"></i></div>
  <div class="abs book"><i class="book-mark"></i>Blog Book</div>
  <div class="abs new-entry"><span class="plus">+</span>Create New Entry</div>
</section>

<section class="abs panel folder">
  <div class="abs folder-label">Folder</div>
  <div class="abs select">Folder name<span><svg width="14" height="10"><path d="M0 0h14L7 9z" fill="#fff"/></svg></span></div>
  <div class="abs folder-bar">
    <div><i></i>Create New Folder</div>
    <div><i></i>Select All Entries</div>
    <div><i></i>Move Selected Folder</div>
  </div>
</section>

<section class="abs panel search">
  <div class="abs search-input">Search blog entry</div>
  <div class="abs search-btn">Search</div>
</section>

<section class="abs panel results">
  <div class="abs result" style="top:0">
    <i class="abs check"></i>
    <h4>Aliquam vehicula mi at mauris</h4>
    <p>Pellentesque habitant morbi tristique senectus et netus et malesuada</p>
    <svg class="abs close" width="18" height="18"><path d="M2 2l14 14M16 2L2 16" stroke="#3a96dc" stroke-width="4"/></svg>
  </div>
  <div class="abs result" style="top:120px">
    <i class="abs check"></i>
    <h4>It took him 7 years to build Plovix.</h4>
    <p>Pellentesque habitant morbi tristique senectus et netus et malesuada</p>
    <svg class="abs close" width="18" height="18"><path d="M2 2l14 14M16 2L2 16" stroke="#3a96dc" stroke-width="4"/></svg>
  </div>
</section>

<section class="abs dark-bar">
  <div class="abs toolbar">
    <span><i class="ico"></i>Pages</span><span><i class="ico"></i>Media</span><span><i class="ico"></i>Messages</span><span><i class="ico"></i>Browse</span><span>→ Apply<i class="x-box"></i></span>
  </div>
  <p class="abs">Pellentesque habitant morbi tristique senectus et netus et malesuada fames ac turpis egestas. In posuere felis nec tortor. Pellentesque faucibus.</p>
  <div class="abs dark-nav"><div>Project</div><div>Team</div><div>Mantra</div><div>Contact</div></div>
</section>

<section class="abs panel gallery">
  <h3 class="abs">Photo Gallery</h3>
  <div class="abs toolbar">
    <span><i class="ico"></i>Pages</span><span><i class="ico"></i>Media</span><span><i class="ico"></i>Messages</span><span><i class="ico"></i>Browse</span><span>→ Apply<i class="x-box"></i></span>
  </div>
  <div class="abs photo" style="left:47px"><div role="img" aria-label="Sunlit forest" style="background:linear-gradient(135deg,#c9a54a,#5f7a2a 55%,#3c5a1f)"></div></div>
  <div class="abs photo" style="left:304px"><div role="img" aria-label="Autumn leaves" style="background:linear-gradient(135deg,#f0c070,#c2541e 55%,#7a2a10)"></div></div>
  <div class="abs photo" style="left:562px"><div role="img" aria-label="Butterfly on a hand against the sky" style="background:linear-gradient(#8fc4ea,#d9ecf8 60%,#c9a58a)"></div></div>
  <div class="abs photo" style="left:819px"><div role="img" aria-label="Fresh green leaves" style="background:linear-gradient(135deg,#e8f6b8,#8dcb3c 55%,#4f9a1c)"></div></div>
</section>

<section class="abs panel comments">
  <div class="abs avatar" style="top:34px"><div role="img" aria-label="Commenter avatar"></div></div>
  <div class="abs bubble" style="top:28px">
    <p>Ut ante enim, dapibus malesuada, fringilla eu, condimentum quis, tellus. Aenean porttitor eros vel dolor. Donec convallis pede venenatis nibh.</p>
    <small>Posted 47 min ago</small>
  </div>
  <div class="abs avatar" style="top:176px"><div role="img" aria-label="Commenter avatar"></div></div>
  <div class="abs bubble" style="top:170px">
    <p>Mauris vel lacus vitae felis vestibulum volutpat. Etiam est nunc, venenatis in, tristique eu, imperdiet ac, nisl.</p>
    <small>Posted 47 min ago</small>
  </div>
  <div class="abs comment-bar">
    <span class="small-btn" style="left:34px">Leave a Comment</span>
    <span class="small-btn" style="right:28px">More blog</span>
  </div>
</section>

<section class="abs calendar">
  <h4><span style="position:absolute;left:16px">‹</span>November 2012<span style="position:absolute;right:16px">›</span></h4>
  <table>
    <tr><th>Su</th><th>Mo</th><th>Tu</th><th>We</th><th>Th</th><th>Fr</th><th>Sa</th></tr>
    <tr><td class="off">28</td><td class="off">29</td><td class="off">30</td><td class="off">31</td><td>1</td><td>2</td><td>3</td></tr>
    <tr><td>4</td><td>5</td><td>6</td><td>7</td><td>8</td><td>9</td><td>10</td></tr>
    <tr><td>11</td><td>12</td><td>13</td><td>14</td><td>15</td><td>16</td><td>17</td></tr>
    <tr><td>18</td><td>19</td><td class="today">20</td><td>21</td><td>22</td><td>23</td><td>24</td></tr>
    <tr><td>25</td><td>26</td><td>27</td><td>28</td><td>29</td><td>30</td><td class="off">1</td></tr>
    <tr><td class="off">2</td><td class="off">3</td><td class="off">4</td><td class="off">5</td><td class="off">6</td><td class="off">7</td><td class="off">8</td></tr>
  </table>
</section>

<section class="abs panel leave">
  <h3 class="abs">Leave a Comment</h3>
  <div class="abs field" style="left:35px;top:70px;width:262px">your name</div>
  <div class="abs field" style="left:329px;top:70px;width:262px">website</div>
  <div class="abs field" style="left:35px;top:126px;width:262px">your email add</div>
  <div class="abs field" style="left:35px;top:182px;width:570px;height:102px">your comment</div>
  <div class="abs submit">SUMIT NOW</div>
</section>

<article class="abs panel post" style="left:67px">
  <h4>Pellentesque habitant morbi tristique senectus netus</h4>
  <p>Pellentesque habitant morbi tristique senectus et netus et malesuada fames ac turpis egestas. In posuere felis nec tortor. Pellentesque faucibus. Ut accumsan ultricies</p>
  <em>Posted on on 04 Feb 2013</em>
  <span class="learn">Learn More</span>
</article>
<article class="abs panel post" style="left:428px">
  <h4>Mauris vel lacus vitae felis vestibulum volutpat</h4>
  <p>Pellentesque habitant morbi tristique senectus et netus et malesuada fames ac turpis egestas. In posuere felis nec tortor. Pellentesque faucibus. Ut accumsan ultricies</p>
  <em>Posted on on 03 Feb 2013</em>
  <span class="learn">Learn More</span>
</article>
<article class="abs panel post" style="left:788px">
  <h4>Etiam est nunc venenatis in tristique eu</h4>
  <p>Pellentesque habitant morbi tristique senectus et netus et malesuada fames ac turpis egestas. In posuere felis nec tortor. Pellentesque faucibus. Ut accumsan ultricies</p>
  <em>Posted on on 06 Feb 2013</em>
  <span class="learn">Learn More</span>
</article>

<section class="abs panel products">
  <div class="abs product" style="left:27px"><div class="pic" role="img" aria-label="Laptop, tablet and phone" style="background:linear-gradient(#cfe6f8,#3a8ee0 60%,#d9d9d9)"></div><h5>Product Name</h5><b>$65.99</b><span class="cart">Add to Cart</span></div>
  <div class="abs product" style="left:281px"><div class="pic" role="img" aria-label="Smartphone" style="background:linear-gradient(135deg,#f7f7f7,#e48ad8 50%,#9ad0f2)"></div><h5>Product Name</h5><b>$65.99</b><span class="cart">Add to Cart</span></div>
  <div class="abs product" style="left:536px"><div class="pic" role="img" aria-label="Smartphone lying flat" style="background:linear-gradient(135deg,#f5f5f5,#5aa8ea 50%,#2a2a2a)"></div><h5>Product Name</h5><b>$65.99</b><span class="cart">Add to Cart</span></div>
  <div class="abs product" style="left:789px"><div class="pic" role="img" aria-label="Stack of smartphones" style="background:linear-gradient(135deg,#f5f5f5,#e0a040 40%,#2a2a2a)"></div><h5>Product Name</h5><b>$65.99</b><span class="cart">Add to Cart</span></div>
</section>

<footer class="abs footer">
  <svg class="abs" style="left:0;top:-10px" width="1200" height="12"><path d="M0 12 L0 6 Q0 6 0 6 M0 12" fill="none"/><pattern id="zig" width="20" height="12" patternUnits="userSpaceOnUse"><path d="M0 12L10 2L20 12z" fill="#3c3c3c"/></pattern><rect width="1200" height="12" fill="url(#zig)"/></svg>
  <div class="abs footer-logo">PLOVIX</div>
  <div class="abs footer-copy">© 2012 Company Name. All right reserved. Term of Use</div>
  <div class="abs toolbar" style="left:608px;top:45px">
    <span><i class="ico"></i>Pages</span><span><i class="ico"></i>Media</span><span><i class="ico"></i>Messages</span><span><i class="ico"></i>Analytics</span><span><i class="ico"></i>Sitemap</span>
  </div>
  <div class="abs toolbar" style="left:608px;top:81px">
    <span><i class="ico"></i>Settings</span><span><i class="ico"></i>Install Apps</span><span><i class="ico"></i>Blog Book</span><span><i class="ico"></i>Browse</span><span>→ Apply</span>
  </div>
</footer>

</body>
</html>
```